co working space / serviced office/ business centre

Brivlo - brivlo.in, is a very young brand bieng run by 3 young entrepreneurs. We want to be become out of the league company delivering fabulous and beautiful serviced offices in India and abroad. We hire designers who have made spaces across the world. We want to get visiting card design which gives complete fresh look to the people who carries that card, has to be very impactful and should symbolise happy young and energetic brand. should be completely out of the box thinking of international level, should portray global brand image.

Target Market(s)

Startups, (Small, medium and large corporates)

Industry/Entity Type

Business

Contact Information for Business Card

Name, Email, Address, Mobile number, Landline number, website

Colors

Designer to choose colors to be used in the design.

Requirements
Must have
• Nice new shape
Nice to have
• We want creative cuts, different size and impactful brand clarity
Should not have
• Boring and regular design and shape

```html
<!DOCTYPE html>
<html lang="en">
<head>
<meta charset="utf-8">
<title>Brivlo business cards</title>
<link rel="stylesheet" href="https://fonts.googleapis.com/css2?family=Lato:wght@300;400;700;900&display=swap">
<style>
  :root {
    --bg: #d2601f;
    --red: #ed1c24;
    --white: #ffffff;
    --panel-grey: #e6e7e8;
    --ink-grey: #7d7e80;
    --ink-light: #a9aaac;
    --logo-grey: #707173;
    --divider-grey: #d3d4d6;
    --rule-red: rgba(255,255,255,0.28);
  }
  * { margin: 0; padding: 0; box-sizing: border-box; }
  html, body { width: 1200px; height: 1200px; overflow: hidden; }
  body {
    background: var(--bg);
    font-family: "Lato", Arial, sans-serif;
    position: relative;
  }
  .card {
    position: absolute;
    width: 518px;
    height: 314px;
  }
  .card-shape { position: absolute; inset: 0; }
  .col-front { left: 54px; }
  .col-back { left: 626px; }
  .row-1 { top: 92px; }
  .row-2 { top: 432px; }
  .row-3 { top: 772px; }

  .brand {
    position: absolute;
    left: 0; right: 0; top: 40px;
    text-align: center;
  }
  .brand-dot {
    width: 20px; height: 20px; border-radius: 50%;
    margin: 0 auto 6px;
  }
  .brand-name {
    display: block;
    font-weight: 900;
    font-size: 30px;
    letter-spacing: 3px;
    line-height: 1;
  }
  .brand-rule {
    width: 169px; height: 2px; margin: 6px auto 7px;
  }
  .brand-tagline {
    display: block;
    font-weight: 900;
    font-size: 10px;
    letter-spacing: 2px;
    text-transform: uppercase;
  }
  .front .brand-dot { background: var(--logo-grey); }
  .front .brand-name { color: var(--logo-grey); }
  .front .brand-rule { background: var(--logo-grey); }
  .front .brand-tagline { color: var(--red); }
  .back .brand-dot { background: var(--white); }
  .back .brand-name, .back .brand-tagline { color: var(--white); }
  .back .brand-rule { background: var(--white); }

  .person {
    position: absolute;
    right: 282px; top: 198px;
    text-align: right;
    color: var(--ink-grey);
  }
  .person-name { font-size: 19px; line-height: 1; letter-spacing: 0.3px; }
  .person-name .first { font-weight: 300; color: var(--ink-light); }
  .person-name .last { font-weight: 400; color: var(--ink-grey); }
  .person-role { font-size: 13px; margin-top: 8px; }
  .divider {
    position: absolute; left: 249px; top: 178px;
    width: 1px; height: 92px; background: var(--divider-grey);
  }
  .contact {
    position: absolute; left: 264px;
    display: flex; align-items: center; gap: 10px;
    font-size: 14px; color: var(--ink-grey);
  }
  .contact svg { flex: none; }
  .contact-phone { top: 200px; }
  .contact-mail { top: 228px; }

  .back-rule {
    position: absolute; left: 96px; right: 96px; height: 1px;
    background: linear-gradient(90deg, transparent, var(--rule-red), transparent);
  }
  .back-rule.upper { top: 184px; }
  .back-rule.lower { top: 242px; }
  .back-line {
    position: absolute;
    display: flex; align-items: center; gap: 7px;
    color: var(--white); font-size: 15px;
  }
  .back-phone { left: 98px; top: 200px; }
  .back-web { left: 278px; top: 200px; }
  .back-address { left: 0; right: 0; top: 252px; justify-content: center; }
</style>
</head>
<body>

<svg width="0" height="0" style="position:absolute">
  <defs>
    <path id="card-outline" d="M24 0 H156 C170 0 175 8 179 18 L183 28 C185 32 189 34 195 34 H323 C329 34 333 32 335 28 L339 18 C343 8 348 0 362 0 H494 A24 24 0 0 1 518 24 V290 A24 24 0 0 1 494 314 H24 A24 24 0 0 1 0 290 V24 A24 24 0 0 1 24 0 Z"/>
    <clipPath id="card-clip"><use href="#card-outline"/></clipPath>
  </defs>
</svg>

<!-- Front cards -->
<div class="card front col-front row-1">
  <svg class="card-shape" viewBox="0 0 518 314" width="518" height="314">
    <g clip-path="url(#card-clip)">
      <rect width="518" height="162" fill="var(--white)"/>
      <rect y="162" width="518" height="130" fill="var(--panel-grey)"/>
      <rect y="292" width="518" height="22" fill="var(--red)"/>
    </g>
  </svg>
  <div class="brand"><div class="brand-dot"></div><span class="brand-name">BRIVLO</span><div class="brand-rule"></div><span class="brand-tagline">Meet. Plan. Grow</span></div>
  <div class="person"><div class="person-name"><span class="first">ROHAN</span><span class="last">MEHTA</span></div><div class="person-role">Founder &amp; COO</div></div>
  <div class="divider"></div>
  <div class="contact contact-phone"><svg width="12" height="18" viewBox="0 0 12 18"><rect x="1" y="1" width="10" height="16" rx="2" fill="none" stroke="var(--ink-grey)" stroke-width="1.6"/><circle cx="6" cy="14" r="1" fill="var(--ink-grey)"/></svg>+91 9876500123</div>
  <div class="contact contact-mail"><svg width="20" height="14" viewBox="0 0 20 14"><rect x="1" y="1" width="18" height="12" fill="none" stroke="var(--ink-grey)" stroke-width="1.6"/><path d="M1 1 L10 8 L19 1 M1 13 L8 6 M19 13 L12 6" fill="none" stroke="var(--ink-grey)" stroke-width="1.4"/></svg>rohan@brivlo.in</div>
</div>

<div class="card front col-front row-2">
  <svg class="card-shape" viewBox="0 0 518 314" width="518" height="314">
    <g clip-path="url(#card-clip)">
      <rect width="518" height="162" fill="var(--white)"/>
      <rect y="162" width="518" height="130" fill="var(--panel-grey)"/>
      <rect y="292" width="518" height="22" fill="var(--red)"/>
    </g>
  </svg>
  <div class="brand"><div class="brand-dot"></div><span class="brand-name">BRIVLO</span><div class="brand-rule"></div><span class="brand-tagline">Meet. Plan. Grow</span></div>
  <div class="person"><div class="person-name"><span class="first">KABIR</span><span class="last">SETHI</span></div><div class="person-role">Founder &amp; CAO</div></div>
  <div class="divider"></div>
  <div class="contact contact-phone"><svg width="12" height="18" viewBox="0 0 12 18"><rect x="1" y="1" width="10" height="16" rx="2" fill="none" stroke="var(--ink-grey)" stroke-width="1.6"/><circle cx="6" cy="14" r="1" fill="var(--ink-grey)"/></svg>+91 9876500123</div>
  <div class="contact contact-mail"><svg width="20" height="14" viewBox="0 0 20 14"><rect x="1" y="1" width="18" height="12" fill="none" stroke="var(--ink-grey)" stroke-width="1.6"/><path d="M1 1 L10 8 L19 1 M1 13 L8 6 M19 13 L12 6" fill="none" stroke="var(--ink-grey)" stroke-width="1.4"/></svg>kabir@brivlo.in</div>
</div>

<div class="card front col-front row-3">
  <svg class="card-shape" viewBox="0 0 518 314" width="518" height="314">
    <g clip-path="url(#card-clip)">
      <rect width="518" height="162" fill="var(--white)"/>
      <rect y="162" width="518" height="130" fill="var(--panel-grey)"/>
      <rect y="292" width="518" height="22" fill="var(--red)"/>
    </g>
  </svg>
  <div class="brand"><div class="brand-dot"></div><span class="brand-name">BRIVLO</span><div class="brand-rule"></div><span class="brand-tagline">Meet. Plan. Grow</span></div>
  <div class="person"><div class="person-name"><span class="first">VIVEK</span><span class="last">ARORA</span></div><div class="person-role">Founder &amp; CEO</div></div>
  <div class="divider"></div>
  <div class="contact contact-phone"><svg width="12" height="18" viewBox="0 0 12 18"><rect x="1" y="1" width="10" height="16" rx="2" fill="none" stroke="var(--ink-grey)" stroke-width="1.6"/><circle cx="6" cy="14" r="1" fill="var(--ink-grey)"/></svg>+91 9876500123</div>
  <div class="contact contact-mail"><svg width="20" height="14" viewBox="0 0 20 14"><rect x="1" y="1" width="18" height="12" fill="none" stroke="var(--ink-grey)" stroke-width="1.6"/><path d="M1 1 L10 8 L19 1 M1 13 L8 6 M19 13 L12 6" fill="none" stroke="var(--ink-grey)" stroke-width="1.4"/></svg>vivek@brivlo.in</div>
</div>

<!-- Back cards -->
<div class="card back col-back row-1">
  <svg class="card-shape" viewBox="0 0 518 314" width="518" height="314"><use href="#card-outline" fill="var(--red)"/></svg>
  <div class="brand"><div class="brand-dot"></div><span class="brand-name">BRIVLO</span><div class="brand-rule"></div><span class="brand-tagline">Meet. Plan. Grow</span></div>
  <div class="back-rule upper"></div><div class="back-rule lower"></div>
  <div class="back-line back-phone"><svg width="28" height="20" viewBox="0 0 28 20"><rect x="1" y="2" width="6" height="17" rx="1" fill="var(--white)"/><rect x="9" y="4" width="18" height="15" rx="1" fill="none" stroke="var(--white)" stroke-width="1.8"/><path d="M13 10h2M17 10h2M21 10h2M13 13h2M17 13h2M21 13h2M13 16h2M17 16h2M21 16h2" stroke="var(--white)" stroke-width="1.6"/></svg>+91 9876500123</div>
  <div class="back-line back-web"><svg width="22" height="22" viewBox="0 0 22 22"><circle cx="10" cy="10" r="8.5" fill="none" stroke="var(--white)" stroke-width="1.6"/><path d="M1.5 10h17M10 1.5v17M4 5h12M4 15h12M10 1.5c-4 4-4 13 0 17M10 1.5c4 4 4 13 0 17" fill="none" stroke="var(--white)" stroke-width="1.2"/><path d="M13 13l8 3-3 1-1 4z" fill="var(--white)"/></svg>www.brivlo.in</div>
  <div class="back-line back-address"><svg width="14" height="20" viewBox="0 0 14 20"><path d="M7 1C3.5 1 1 3.6 1 7c0 4.5 6 12 6 12s6-7.5 6-12c0-3.4-2.5-6-6-6z" fill="none" stroke="var(--white)" stroke-width="2"/><circle cx="7" cy="7" r="2.2" fill="var(--white)"/></svg>Block 7A Tech Park, Sector 21</div>
</div>

<div class="card back col-back row-2">
  <svg class="card-shape" viewBox="0 0 518 314" width="518" height="314"><use href="#card-outline" fill="var(--red)"/></svg>
  <div class="brand"><div class="brand-dot"></div><span class="brand-name">BRIVLO</span><div class="brand-rule"></div><span class="brand-tagline">Meet. Plan. Grow</span></div>
  <div class="back-rule upper"></div><div class="back-rule lower"></div>
  <div class="back-line back-phone"><svg width="28" height="20" viewBox="0 0 28 20"><rect x="1" y="2" width="6" height="17" rx="1" fill="var(--white)"/><rect x="9" y="4" width="18" height="15" rx="1" fill="none" stroke="var(--white)" stroke-width="1.8"/><path d="M13 10h2M17 10h2M21 10h2M13 13h2M17 13h2M21 13h2M13 16h2M17 16h2M21 16h2" stroke="var(--white)" stroke-width="1.6"/></svg>+91 9876500123</div>
  <div class="back-line back-web"><svg width="22" height="22" viewBox="0 0 22 22"><circle cx="10" cy="10" r="8.5" fill="none" stroke="var(--white)" stroke-width="1.6"/><path d="M1.5 10h17M10 1.5v17M4 5h12M4 15h12M10 1.5c-4 4-4 13 0 17M10 1.5c4 4 4 13 0 17" fill="none" stroke="var(--white)" stroke-width="1.2"/><path d="M13 13l8 3-3 1-1 4z" fill="var(--white)"/></svg>www.brivlo.in</div>
  <div class="back-line back-address"><svg width="14" height="20" viewBox="0 0 14 20"><path d="M7 1C3.5 1 1 3.6 1 7c0 4.5 6 12 6 12s6-7.5 6-12c0-3.4-2.5-6-6-6z" fill="none" stroke="var(--white)" stroke-width="2"/><circle cx="7" cy="7" r="2.2" fill="var(--white)"/></svg>Block 7A Tech Park, Sector 21</div>
</div>

<div class="card back col-back row-3">
  <svg class="card-shape" viewBox="0 0 518 314" width="518" height="314"><use href="#card-outline" fill="var(--red)"/></svg>
  <div class="brand"><div class="brand-dot"></div><span class="brand-name">BRIVLO</span><div class="brand-rule"></div><span class="brand-tagline">Meet. Plan. Grow</span></div>
  <div class="back-rule upper"></div><div class="back-rule lower"></div>
  <div class="back-line back-phone"><svg width="28" height="20" viewBox="0 0 28 20"><rect x="1" y="2" width="6" height="17" rx="1" fill="var(--white)"/><rect x="9" y="4" width="18" height="15" rx="1" fill="none" stroke="var(--white)" stroke-width="1.8"/><path d="M13 10h2M17 10h2M21 10h2M13 13h2M17 13h2M21 13h2M13 16h2M17 16h2M21 16h2" stroke="var(--white)" stroke-width="1.6"/></svg>+91 9876500123</div>
  <div class="back-line back-web"><svg width="22" height="22" viewBox="0 0 22 22"><circle cx="10" cy="10" r="8.5" fill="none" stroke="var(--white)" stroke-width="1.6"/><path d="M1.5 10h17M10 1.5v17M4 5h12M4 15h12M10 1.5c-4 4-4 13 0 17M10 1.5c4 4 4 13 0 17" fill="none" stroke="var(--white)" stroke-width="1.2"/><path d="M13 13l8 3-3 1-1 4z" fill="var(--white)"/></svg>www.brivlo.in</div>
  <div class="back-line back-address"><svg width="14" height="20" viewBox="0 0 14 20"><path d="M7 1C3.5 1 1 3.6 1 7c0 4.5 6 12 6 12s6-7.5 6-12c0-3.4-2.5-6-6-6z" fill="none" stroke="var(--white)" stroke-width="2"/><circle cx="7" cy="7" r="2.2" fill="var(--white)"/></svg>Block 7A Tech Park, Sector 21</div>
</div>

</body>
</html>
```